The Brightwater Compass Business Card

We need an attractive business card with the logo that we bought from ArtVantly last year.
Our mission is to contribute to change the way today's leaders manage business companies bringing value to the workplace and helping them to build a new model of creating wealth.
Our logo is clear about our values : we seek Positive Change through People and are convinced that the pursuit of individual well-being and the chase of economic results can converge with the right management.
Management Consulting
Corinne Fabrelle
+34 612 98 70 31
corinne.fabrelle@thebrightwatercompass-mail.net
www.thebrightwatercompass-mail.net

```html
<!DOCTYPE html>
<html lang="en">
<head>
<meta charset="utf-8">
<title>The Brightwater Compass – Business Card</title>
<link rel="stylesheet" href="https://fonts.googleapis.com/css2?family=Cinzel:wght@500&family=Marcellus&family=Marcellus+SC&display=swap">
<style>
  :root {
    --page-bg: #e6e7e8;
    --card-white: #ffffff;
    --teal: #0f8580;
    --teal-text: #148a84;
    --teal-rule: #b9dcda;
    --navy: #12303b;
    --white: #ffffff;
    --shadow: rgba(0, 0, 0, 0.28);
  }
  * { margin: 0; padding: 0; box-sizing: border-box; }
  html, body {
    width: 1200px; height: 1200px; overflow: hidden;
    background: var(--page-bg);
  }
  .canvas { position: relative; width: 1200px; height: 1200px; }

  .card {
    position: absolute;
    border-radius: 28px;
    overflow: hidden;
    box-shadow: 0 18px 26px -10px var(--shadow);
  }

  /* Front */
  .card-front {
    left: 190px; top: 57px; width: 828px; height: 493px;
    background: var(--card-white);
  }
  .front-brand {
    position: absolute; left: 48px; top: 58px; width: 360px;
    display: flex; flex-direction: column; align-items: center; gap: 18px;
  }
  .brand-dot {
    width: 64px; height: 64px; border-radius: 50%;
    background: var(--teal);
  }
  .brand-name {
    font-family: "Cinzel", serif; font-weight: 500;
    font-size: 31px; line-height: 1.15; text-align: center;
    color: var(--teal-text); letter-spacing: 0.5px;
  }
  .person-name {
    position: absolute; left: 68px; top: 272px;
    font-family: "Marcellus SC", serif; font-size: 40px;
    color: var(--teal-text); letter-spacing: 0.5px;
  }
  .contact-band {
    position: absolute; left: 0; right: 0; top: 333px; bottom: 0;
    background: var(--teal);
    border-top: 3px solid var(--teal-rule);
  }
  .contact-list { list-style: none; position: absolute; left: 28px; top: 26px; }
  .contact-item {
    display: flex; align-items: center; gap: 16px;
    height: 48px; margin-bottom: 6px;
    font-family: "Marcellus", serif; color: var(--white);
  }
  .contact-item.phone { font-size: 29px; }
  .contact-item.email { font-size: 26px; }
  .contact-icon { width: 48px; height: 48px; flex: none; }

  /* Back */
  .card-back {
    left: 194px; top: 607px; width: 814px; height: 498px;
    background: var(--navy);
    display: flex; flex-direction: column; align-items: center;
    padding-top: 118px;
  }
  .card-back .brand-dot { width: 96px; height: 96px; background: var(--white); }
  .card-back .brand-name {
    color: var(--white); font-size: 44px; margin-top: 28px; white-space: nowrap;
  }
  .website {
    margin-top: 26px;
    font-family: "Marcellus", serif; font-size: 30px; color: var(--white);
  }
</style>
</head>
<body>
<main class="canvas">

  <section class="card card-front" aria-label="Business card front">
    <div class="front-brand">
      <span class="brand-dot" aria-hidden="true"></span>
      <p class="brand-name">The Brightwater Compass</p>
    </div>
    <h1 class="person-name">Corinne Fabrelle</h1>

    <div class="contact-band">
      <ul class="contact-list">
        <li class="contact-item phone">
          <svg class="contact-icon" viewBox="0 0 48 48" aria-hidden="true">
            <circle cx="24" cy="24" r="24" fill="#ffffff"/>
            <path d="M16 12c1-1 2.6-1 3.4 0l3 4c.7.9.5 2.1-.3 2.8l-1.7 1.5c1.4 3 3.6 5.3 6.5 6.8l1.6-1.7c.7-.8 2-.9 2.8-.2l4 3c1 .8 1 2.3.1 3.3l-2 2c-1.4 1.4-3.6 1.7-5.4.8C21.500 31.900 16.200 26.600 13.700 20c-.8-1.900-.4-4 1-5.400z" fill="#0f8580"/>
          </svg>
          <span>+34 612 98 70 31</span>
        </li>
        <li class="contact-item email">
          <svg class="contact-icon" viewBox="0 0 48 48" aria-hidden="true">
            <circle cx="24" cy="24" r="24" fill="#ffffff"/>
            <rect x="12" y="15" width="24" height="18" rx="1.5" fill="none" stroke="#0f8580" stroke-width="2.4"/>
            <path d="M12.5 16l11.5 9.5L35.5 16M12.5 32.5l8.5-8M35.5 32.5l-8.5-8" fill="none" stroke="#0f8580" stroke-width="2.2"/>
          </svg>
          <span>corinne.fabrelle@thebrightwatercompass-mail.net</span>
        </li>
      </ul>
    </div>
  </section>

  <section class="card card-back" aria-label="Business card back">
    <span class="brand-dot" aria-hidden="true"></span>
    <p class="brand-name">The Brightwater Compass</p>
    <p class="website">www.thebrightwatercompass-mail.net</p>
  </section>

</main>
</body>
</html>
```